Sheep ranch business card design

We need a business card design for our farm. We do all things sheep. We run Babydoll southdown sheep and use their fiber and meat. In the spring the lambs are sold. We shear them for their wool to make dryer balls, roving, and yarn which we sell. We also lease the sheep out to organic vineyards in the winter time to help them convert their weeds and cover crops to manure so they don't have to use tractors and tillers to mow and compact soil. Fennick Ranch also breeds Kangals which are livestock guard dogs that live with and protect the sheep. We also run a small herd of jersey cows, chickens, and bees but the sheep enterprise is the focal point. I would like to see the design use more earth tones and natural colors and have the feel of a modern and hip farm. I would also like our attached fennick ranch image to be used. The font family is dalle for our logo. That font can be used or something to compliment it. The attached pictures can be used as well but they are not necessary. One fennick ranch upload is in psd and one is in jpeg. Thank You and we look forward to seeing your work.
Updates

So many great designs. Not looking for anything "western." Font, design, or otherwise.

Industry/Entity Type

Livestock

Contact Information for Business Card

Fennick Ranch
Corin Fennick
www.fennickranch-example.com
fennickranch@mailbox-example.com
phone: 555 310-7282

```html
<!DOCTYPE html>
<html lang="en">
<head>
<meta charset="utf-8">
<title>Fennick Ranch – Business Card</title>
<link href="https://fonts.googleapis.com/css2?family=Lato:wght@400;700;900&display=swap" rel="stylesheet">
<style>
  :root {
    --backdrop: #2c2c2c;
    --card: #f3f3f2;
    --ink: #262626;
    --ink-soft: #4a4a4a;
    --ink-muted: #666666;
    --rule: #2f2f2f;
  }
  * { margin: 0; padding: 0; box-sizing: border-box; }
  html, body {
    width: 1200px;
    height: 1116px;
    overflow: hidden;
    background: var(--backdrop);
    font-family: "Lato", Arial, sans-serif;
  }
  .stage {
    width: 1200px;
    height: 1116px;
    display: flex;
    align-items: center;
    justify-content: center;
  }
  .business-card {
    position: relative;
    width: 960px;
    height: 548px;
    background: var(--card);
    border-radius: 30px;
    color: var(--ink);
  }
  .brand {
    position: absolute;
    left: 78px;
    top: 150px;
    display: flex;
    align-items: center;
    gap: 18px;
  }
  .brand-dot {
    width: 34px;
    height: 34px;
    border-radius: 50%;
    background: var(--ink);
  }
  .brand-name {
    font-size: 50px;
    font-weight: 400;
    letter-spacing: 9px;
    text-transform: uppercase;
    color: var(--ink);
    line-height: 1;
  }
  .holder {
    position: absolute;
    right: 86px;
    top: 228px;
    text-align: right;
  }
  .holder-name {
    font-size: 27px;
    font-weight: 900;
    color: var(--ink);
    line-height: 1.1;
  }
  .holder-role {
    font-size: 15px;
    font-weight: 400;
    letter-spacing: 1.5px;
    color: var(--ink-muted);
    margin-top: 4px;
    padding-bottom: 6px;
    border-bottom: 3px solid var(--rule);
  }
  .divider {
    position: absolute;
    left: 78px;
    right: 86px;
    top: 300px;
    height: 2px;
    background: var(--rule);
  }
  .contact-list {
    position: absolute;
    left: 78px;
    top: 356px;
    list-style: none;
  }
  .contact-item {
    display: flex;
    align-items: center;
    gap: 18px;
    font-size: 20px;
    font-weight: 700;
    color: var(--ink-soft);
    height: 46px;
  }
  .contact-icon {
    width: 24px;
    height: 24px;
    flex: none;
    fill: var(--ink-soft);
    stroke: var(--ink-soft);
  }
</style>
</head>
<body>
<main class="stage">
  <article class="business-card">
    <div class="brand">
      <span class="brand-dot"></span>
      <span class="brand-name">Fennick Ranch</span>
    </div>

    <div class="holder">
      <p class="holder-name">Corin Fennick</p>
      <p class="holder-role">OWNER / FOUNDER</p>
    </div>

    <div class="divider"></div>

    <ul class="contact-list">
      <li class="contact-item">
        <svg class="contact-icon" viewBox="0 0 24 24" aria-hidden="true" stroke-width="0">
          <path d="M3 9c0-3 4-5 9-5s9 2 9 5v2h-5V8.5c-1.5-.6-6.5-.6-8 0V11H3z"/>
          <path d="M7 12h10l2 8H5z"/>
        </svg>
        <span>555 310-7282</span>
      </li>
      <li class="contact-item">
        <svg class="contact-icon" viewBox="0 0 24 24" aria-hidden="true" fill="none" stroke-width="2.4" stroke-linecap="round">
          <path d="M10 14a4 4 0 0 0 5.7 0l3.5-3.5a4 4 0 0 0-5.7-5.7L12 6.3" style="fill:none"/>
          <path d="M14 10a4 4 0 0 0-5.7 0l-3.5 3.5a4 4 0 0 0 5.7 5.7l1.5-1.5" style="fill:none"/>
        </svg>
        <span>www.fennickranch-example.com</span>
      </li>
      <li class="contact-item">
        <svg class="contact-icon" viewBox="0 0 24 24" aria-hidden="true" stroke-width="0">
          <path d="M2 5h20v14H2z"/>
          <path d="M3.5 6.5l8.5 7 8.5-7" style="fill:none;stroke:var(--card);stroke-width:1.8"/>
        </svg>
        <span>fennickranch@mailbox-example.com</span>
      </li>
    </ul>
  </article>
</main>
</body>
</html>
```